New Business Card

We need to refresh our business cards. We designed these ourselves and we have no graphic design experience. We would like to find a new business card design that is professional and unique. We are an auto finance company. Feel free to play with the logo, but we would like to keep the eye very present on the card. Our corporate colors are green, grey, and white.
Green - RGB - 168,215,27; HEX - #AADD22
Grey - RGB - 196,196,196; HEX - #C4C4C4
Updates
Need to upload the vector file to finalize the project. The last logo was for a jpeg that didn't stretch well.
Industry/Entity Type
Financial Service
Contact Information for Business Card
Honestly don't know...I need your help!

```html
<!DOCTYPE html>
<html lang="en">
<head>
<meta charset="utf-8">
<title>Brightpath Capital – Business Card</title>
<link rel="stylesheet" href="https://fonts.googleapis.com/css2?family=Source+Sans+3:wght@400;600&family=Arimo:wght@400;700&display=swap">
<style>
  :root {
    --stage: #767676;
    --green: #aadd22;
    --green-deep: #97c514;
    --black: #000000;
    --white: #ffffff;
    --grey: #c4c4c4;
    --ink: #111111;
  }
  * { box-sizing: border-box; margin: 0; padding: 0; }
  html, body { width: 1200px; height: 900px; overflow: hidden; }
  body {
    background: var(--stage);
    position: relative;
    font-family: "Source Sans 3", Arial, sans-serif;
  }
  .card {
    position: absolute;
    top: 306px;
    width: 440px;
    height: 271px;
    border-radius: 10px;
    overflow: hidden;
  }
  /* Front */
  .card-front {
    left: 149px;
    background: var(--green);
    box-shadow: 3px 4px 6px rgba(0,0,0,0.45);
  }
  .front-header {
    position: absolute;
    left: 0; top: 0;
    width: 100%; height: 117px;
    background: var(--black);
  }
  .wordmark {
    color: var(--green);
    font-weight: 600;
    line-height: 1;
  }
  .front-header .wordmark {
    position: absolute;
    left: 20px; top: 26px;
  }
  .wordmark-main { display: block; font-size: 44px; letter-spacing: -0.5px; }
  .wordmark-sub { display: block; font-size: 15px; letter-spacing: 9px; margin-top: 10px; padding-left: 16px; }
  .holder {
    position: absolute;
    right: 22px; top: 46px;
    text-align: right;
    font-family: "Arimo", Arial, sans-serif;
  }
  .holder-name { color: var(--green); font-weight: 700; font-size: 16px; }
  .holder-title { color: var(--white); font-size: 12px; margin-top: 3px; }
  .contact {
    position: absolute;
    left: 22px; top: 146px;
    color: var(--white);
    font-size: 12.5px;
    line-height: 16px;
    list-style: none;
  }
  .contact li { display: flex; align-items: center; gap: 6px; }
  .contact svg { width: 10px; height: 10px; flex: none; }
  .address {
    position: absolute;
    left: 21px; top: 214px;
    color: var(--white);
    font-size: 12.5px;
    line-height: 16px;
  }
  .front-mark {
    position: absolute;
    left: 232px; top: 130px;
    width: 184px; height: 118px;
  }
  /* Back */
  .card-back {
    left: 608px;
    background: var(--white);
  }
  .back-band-top {
    position: absolute; left: 0; top: 0;
    width: 100%; height: 16px;
    background: var(--black);
  }
  .back-band-bottom {
    position: absolute; left: 0; bottom: 0;
    width: 100%; height: 14px;
    background: var(--green);
  }
  .back-brand {
    position: absolute;
    left: 0; top: 80px;
    width: 100%;
    display: flex; flex-direction: column; align-items: center;
  }
  .back-dot {
    width: 54px; height: 54px;
    border-radius: 50%;
    background: var(--green);
    margin-bottom: 22px;
  }
  .back-brand .wordmark { text-align: center; }
  .back-brand .wordmark-main { font-size: 42px; }
  .back-brand .wordmark-sub { font-size: 14px; letter-spacing: 8px; padding-left: 8px; margin-top: 9px; }
</style>
</head>
<body>
  <section class="card card-front">
    <header class="front-header">
      <div class="wordmark">
        <span class="wordmark-main">Brightpath</span>
        <span class="wordmark-sub">CAPITAL</span>
      </div>
      <div class="holder">
        <div class="holder-name">Daniel Reyes</div>
        <div class="holder-title">Managing Director</div>
      </div>
    </header>

    <svg class="front-mark" viewBox="0 0 184 118" aria-hidden="true">
      <circle cx="92" cy="59" r="56" fill="var(--green-deep)"/>
    </svg>

    <ul class="contact">
      <li>
        <svg viewBox="0 0 10 10"><rect x="2.5" y="0.5" width="5" height="9" rx="1" fill="none" stroke="#fff" stroke-width="1"/><circle cx="5" cy="8" r="0.6" fill="#fff"/></svg>
        044-123 456 789
      </li>
      <li>
        <svg viewBox="0 0 10 10"><path d="M1 4 Q5 1 9 4 L8 5 L6.5 4 V3.3 Q5 3 3.5 3.3 V4 L2 5 Z" fill="#fff"/><rect x="2" y="5.5" width="6" height="3.5" rx="0.6" fill="#fff"/></svg>
        044-123 456 789
      </li>
      <li>
        <svg viewBox="0 0 10 10"><rect x="0.5" y="2" width="9" height="6" fill="#fff"/><path d="M0.5 2 L5 5.5 L9.5 2" fill="none" stroke="var(--green)" stroke-width="0.8"/></svg>
        info@webname.com
      </li>
      <li>
        <svg viewBox="0 0 10 10"><circle cx="5" cy="5" r="4.5" fill="#fff"/><path d="M3 3 Q5 4 4 6 Q6 6 7 8" fill="none" stroke="var(--green)" stroke-width="1"/></svg>
        www.websitename.com
      </li>
    </ul>
    <p class="address">12345, Address Goes Here<br>Country Name, 123456.</p>
  </section>

  <section class="card card-back">
    <div class="back-band-top"></div>
    <div class="back-brand">
      <div class="back-dot"></div>
      <div class="wordmark">
        <span class="wordmark-main">Brightpath</span>
        <span class="wordmark-sub">CAPITAL</span>
      </div>
    </div>
    <div class="back-band-bottom"></div>
  </section>
</body>
</html>
```